Wohnhof am Weiher - Zeitungsinserat für den Verkauf von Eigentumswohnungen

Wir brauchen ein Zeitungsinserat in zwei Formaten. Einmal 296 Breite x 440 Höhe mm und einmal 296 Breite x 220 mm Höhe.
Als Basis dient der sehr grobe Entwurf im Powerpoint (Entwurf.pptx).
Auf dem Entwurf fehlen noch die Kontaktangeben:
Brunnhofer Liegenschaften AG
Seematteweg 14
4387 Tannried
079 462 37 58
rbrunnhofer@tessin-ostwald.ch

Zudem muss noch der Link auf die Webseite aufgeführt werden.
www.wohnhof-am-weiher.ch

Zudem fehlt noch der Text:
Fordern Sie noch heute die Verkaufsunterlagen gedruckt oder per Email an. Schreiben Sie uns einfach eine Chatpost mit Ihrer Adresse.

Ich habe noch Files von den Innenvisualisierungen, den Aussenvisualisierungen sowie unser Logo hinzugefügt. Zudem habe ich Ihnen die Verkaufsbrochure angefügt. Sie können die Daten vom Entwurf gerne ergänzen wenn Ihnen etwas gefällt. Schön wäre es, wenn Sie den Stil ähnlich machen würden wie die Brochure.

Target Market(s)

Famillien, Paare und Rentner

Font styles to use
Serif

Colors

Designer to choose colors to be used in the design.

Requirements
Must have
• Tolles Design das sofort anspricht!

```html
<!DOCTYPE html>
<html lang="de">
<head>
<meta charset="utf-8">
<title>Wohnhof am Weiher – Inserat</title>
<link href="https://fonts.googleapis.com/css2?family=Montserrat:wght@700;800&family=Gelasio:wght@400;500;600&family=Poppins:wght@400;500&display=swap" rel="stylesheet">
<style>
:root{
  --stage:#d6d6d6;
  --paper:#ffffff;
  --brand-blue:#03729a;
  --brand-red:#ee2a34;
  --ink:#1b1b1b;
  --col-bg:#e3e3e3;
  --tag-cyan:#00e6f4;
  --tag-red:#f34a5b;
  --tag-green:#1ff0b2;
  --tag-sky:#6db6f8;
  --tag-violet:#8ba6ef;
}
*{box-sizing:border-box;margin:0;padding:0}
html,body{width:1200px;height:1200px;overflow:hidden;background:var(--stage)}
.ad{position:absolute;left:196px;top:0;width:808px;height:1200px;background:var(--paper);overflow:hidden;color:var(--ink)}
.brand{position:absolute;left:40px;top:62px;display:flex;align-items:center;gap:8px;font-family:"Gelasio",serif;font-weight:600;font-size:18px;color:var(--brand-blue);line-height:1.15}
.brand-mark{width:14px;height:14px;background:var(--brand-blue);flex:none}
.title{position:absolute;left:332px;top:28px;font-family:"Montserrat",sans-serif;font-weight:800;font-size:44px;line-height:1;letter-spacing:0.5px}
.title .l1{color:var(--brand-blue);display:block}
.title .l2{color:var(--brand-red);font-weight:700;display:block;margin-top:4px}
.subtitle{position:absolute;left:333px;top:136px;font-family:"Gelasio",serif;font-weight:600;font-size:15.5px}
.corner{position:absolute;right:0;top:0;width:73px;height:163px;background:var(--brand-blue)}
.photo{position:absolute}
.photo-out{left:0;top:175px;width:391px;height:183px;background:linear-gradient(180deg,#8cb6dc 0%,#c9dcec 45%,#b9bcbc 62%,#6d9a55 85%,#5b8a45 100%)}
.photo-in{left:405px;top:170px;width:403px;height:189px;background:linear-gradient(180deg,#f4f4f4 0%,#e4e2df 55%,#b9b2a8 80%,#c7915a 100%)}
.photo-strip{position:absolute;left:735px;top:359px;width:73px;height:9px;background:var(--brand-blue)}
.info{position:absolute;left:40px;width:318px;font-family:"Poppins",sans-serif;font-size:10.2px;line-height:1.22}
.info h2{font-family:"Gelasio",serif;font-weight:500;font-size:19.5px;line-height:1.2;margin-bottom:9px}
.cta{position:absolute;left:40px;top:1187px}
.footer{position:absolute;left:0;top:1088px;width:808px;height:112px;background:var(--brand-blue);color:#fff;font-family:"Poppins",sans-serif}
.contact{position:absolute;left:40px;display:flex;gap:10px;align-items:flex-start;font-size:12.5px;line-height:1.25}
.contact svg{flex:none}
.contact.small{font-size:10.5px}
.web{position:absolute;left:512px;top:1160px;font-family:"Poppins",sans-serif;font-size:13.5px;letter-spacing:1.6px;color:#fff}
.haus{position:absolute;left:387px;width:387px;text-align:center;font-family:"Gelasio",serif;font-weight:500;font-size:14px}
.units{position:absolute;left:387px;width:386px;height:232px;display:grid;grid-template-columns:74px 74px 50px 97px 75px;gap:4px;font-family:"Gelasio",serif;font-size:11.2px;line-height:1.15}
.units.last{background:var(--paper);padding:0 4px 8px;left:381px;width:394px;height:242px;border-radius:0 0 6px 6px}
.col{background:var(--col-bg);border-radius:5px;padding:3px;display:flex;flex-direction:column}
.tag{border-radius:5px;padding:4px 6px;min-height:33px;display:flex;align-items:center;font-weight:500}
.tag.cyan{background:var(--tag-cyan);font-size:13px}
.tag.red{background:var(--tag-red)}
.tag.green{background:var(--tag-green)}
.tag.sky{background:var(--tag-sky);min-height:48px}
.tag.violet{background:var(--tag-violet)}
.rows{flex:1;display:flex;flex-direction:column;justify-content:space-around;padding:6px 6px 4px}
.rows span{display:block;overflow-wrap:anywhere}
sup{font-size:0.65em}
</style>
</head>
<body>
<div class="ad">
  <div class="brand"><span class="brand-mark"></span><span>Brunnhofer<br>Liegenschaften AG</span></div>
  <h1 class="title"><span class="l1">WOHNHOF</span><span class="l2">AM WEIHER</span></h1>
  <p class="subtitle">Hochwertige und moderne Eigentumswohnungen</p>
  <div class="corner"></div>

  <div class="photo photo-out" role="img" aria-label="Aussenvisualisierung der Wohnanlage mit Bäumen und Wiese"></div>
  <div class="photo photo-in" role="img" aria-label="Innenvisualisierung: Wohnraum mit offener Küche"></div>
  <div class="photo-strip"></div>

  <section class="info" style="top:397px"><h2>Bus und Bahn</h2><p>Lorem Ipsum is simply dummy text of the printing and typesetting industry. Lorem Ipsum has been the industry's standard dummy text ever since the 1500s, when an unknown printer took a galley of type and scrambled it to make</p></section>
  <section class="info" style="top:515px"><h2>Basel - Stadit</h2><p>Lorem Ipsum is simply dummy text of the printing and typesetting industry. Lorem Ipsum has been the industry's standard dummy text ever since the 1500s, when an unknown printer took a galley of type and scrambled it to make</p></section>
  <section class="info" style="top:630px"><h2>Autobahn</h2><p>Lorem Ipsum is simply dummy text of the printing and typesetting industry. Lorem Ipsum has been the industry's standard dummy text ever since the 1500s, when an unknown printer took a galley of type and scrambled it to make</p></section>
  <section class="info" style="top:743px"><h2>Einkaufen und weitere Dienstleistungen</h2><p>Lorem Ipsum is simply dummy text of the printing and typesetting industry. Lorem Ipsum has been the industry's standard dummy text ever since the 1500s, when an unknown printer took a galley of type and scrambled it to make</p></section>
  <section class="info" style="top:878px"><h2>Einkaufen und weitere Dienstleistungen</h2><p>Lorem Ipsum is simply dummy text of the printing and typesetting industry. Lorem Ipsum has been the industry's standard dummy text ever since the 1500s, when an unknown printer took a galley of type and scrambled it to make</p></section>
  <p class="info" style="top:1027px">Fordern Sie noch heute die Verkaufsunterlagen gedruckt oder per Email an. Schreiben Sie uns einfach eine Chatpost mit Ihrer Adresse.</p>

  <footer class="footer">
    <div class="contact" style="top:10px">
      <svg width="18" height="20" viewBox="0 0 18 20"><rect x="1" y="1" width="16" height="18" rx="4" fill="#fff"/><path d="M6 5c-1 1-1 4 1 7s4 4 5 3l-1.5-2-1.5.7c-1-.8-2-2.6-2-3.7l1.3-.8L7.5 5z" fill="var(--brand-blue)"/></svg>
      <span>4387 Tannried<br>079 462 37 58</span>
    </div>
    <div class="contact small" style="top:60px">
      <svg width="18" height="12" viewBox="0 0 18 12"><rect x="1" y="1" width="16" height="10" fill="none" stroke="#fff" stroke-width="1.6"/><path d="M1 1l8 6 8-6" fill="none" stroke="#fff" stroke-width="1.6"/></svg>
      <span>rbrunnhofer@tessin-ostwald.ch</span>
    </div>
    <div class="contact small" style="top:80px;font-size:9.8px">
      <svg width="16" height="20" viewBox="0 0 16 20"><path d="M8 1a7 7 0 0 0-7 7c0 5 7 11 7 11s7-6 7-11a7 7 0 0 0-7-7z" fill="#fff"/><circle cx="8" cy="8" r="2.6" fill="var(--brand-blue)"/></svg>
      <span>Brunnhofer Liegenschaften AG<br>Seematteweg 14</span>
    </div>
  </footer>
  <div class="web">www.wohnhof-am-weiher.ch</div>

  <div class="haus" style="top:369px">Haus A</div>
  <div class="units" style="top:388px">
    <div class="col"><div class="tag cyan">Attika</div><div class="rows"><span>Obergeschoss</span><span>Obergeschoss</span><span>Erdgeschoss</span><span>Erdgeschoss</span></div></div>
    <div class="col"><div class="tag red">4.5 Zimmer</div><div class="rows"><span>2.5 Zimmer</span><span>4.5 Zimmer</span><span>2.5 Zimmer</span><span>3.5 Zimmer</span></div></div>
    <div class="col"><div class="tag green">109m2</div><div class="rows"><span>81m<sup>2</sup></span><span>102m</span><span>81m2</span><span>102m</span></div></div>
    <div class="col"><div class="tag sky">105m Sonnenterrasse</div><div class="rows"><span>16m2 Balkon</span><span>33m2 Balkon</span><span>16m2 gedeckter Sitzplatz &amp; eigener Garten</span><span>33m2 gedeckter Sitzplatz &amp; eigener Garten</span></div></div>
    <div class="col"><div class="tag violet">945’000 CHF</div><div class="rows"><span>754’800 CHF</span><span>640’000 CHF</span><span>657’000 CHF</span><span>765’000 CHF</span></div></div>
  </div>

  <div class="haus" style="top:623px">Haus A</div>
  <div class="units" style="top:646px">
    <div class="col"><div class="tag cyan">Attika</div><div class="rows"><span>Obergeschoss</span><span>Obergeschoss</span><span>Erdgeschoss</span><span>Erdgeschoss</span></div></div>
    <div class="col"><div class="tag red">4.5 Zimmer</div><div class="rows"><span>2.5 Zimmer</span><span>4.5 Zimmer</span><span>2.5 Zimmer</span><span>4.5 Zimmer</span></div></div>
    <div class="col"><div class="tag green">109m2</div><div class="rows"><span>69m<sup>2</sup></span><span>117m</span><span>69m2</span><span>117m2</span></div></div>
    <div class="col"><div class="tag sky">107m2 Sonnenterrasse</div><div class="rows"><span>14 m<sup>2</sup> Balkon</span><span>42 m<sup>2</sup> Balkon</span><span>14m<sup>2</sup> gedeckter Sitzplatz &amp; eigener Garten</span><span>42m<sup>2</sup> gedeckter Sitzplatz &amp; eigener Garten</span></div></div>
    <div class="col"><div class="tag violet">965’000 CHF</div><div class="rows"><span>550’000 CHF</span><span>877’500 CHF</span><span>560’000 CHF</span><span>889’000 CHF</span></div></div>
  </div>

  <div class="haus" style="top:884px">Haus A</div>
  <div class="units last" style="top:904px">
    <div class="col"><div class="tag cyan">Attika</div><div class="rows"><span>Obergeschoss</span><span>Obergeschoss</span><span>Erdgeschoss</span><span>Erdgeschoss</span></div></div>
    <div class="col"><div class="tag red">4.5 Zimmer</div><div class="rows"><span>5.5 Zimmer</span><span>3.5 Zimmer</span><span>5.5 Zimmer</span><span>3.5 Zimmer</span></div></div>
    <div class="col"><div class="tag green">109m2</div><div class="rows"><span>129m<sup>2</sup></span><span>143m<sup>2</sup></span><span>143m<sup>2</sup></span><span>96m<sup>2</sup></span></div></div>
    <div class="col"><div class="tag sky">107m2 Sonnenterrasse</div><div class="rows"><span>14 m<sup>2</sup> Balkon</span><span>42 m<sup>2</sup> Balkon</span><span>14m<sup>2</sup> gedeckter Sitzplatz &amp; eigener Garten</span><span>42m<sup>2</sup> gedeckter Sitzplatz &amp; eigener Garten</span></div></div>
    <div class="col"><div class="tag violet">965’000 CHF</div><div class="rows"><span>550’000 CHF</span><span>877’500 CHF</span><span>560’000 CHF</span><span>889’000 CHF</span></div></div>
  </div>
</div>
</body>
</html>
```